Pause Your Day And Browse- PYDB poster

I am the Vice President of Advocacy for the Coastline Shelfkeepers Guild. I am looking to have a set of posters made for PYDB (Pause Your Day and Browse) October 23. PYDB is a time when all school children in BC are encouraged to Pause Your Day and Browse for 15-20 minutes at some point in their day.

I would like to get a set of 2 digital posters designed (if possible it would be nice to have the option to print to both 11 x 17 and 8.5 x 11 paper). We need a poster that is high school (Grade 8-12) appropriate and one that is elementary (Grade k-7) appropriate. Both posters need to be replicated in French. All posters need to have the KWNU logo on them as well as the Coastline Shelfkeepers Guild Logo.

Here is a link to last year's successful design http://kwnu-example.org/csg/info/advocacy.html
There are two additional samples in the uploaded files section.

Each poster needs to have the following information:

-Pause Your Day and Browse (PYDB)
- The date Monday, October 23, 2017
-the logo for the KWNU (attached)
-the logo for the CSG (attached)- the logos do not have to be large.

Target Market(s)

Children ages 5-12 and 12-17 as well as their teachers

Industry/Entity Type

Teacher

Font styles to use
Sans Serif

Requirements
Must have
• Must have both logos- colours may be changed for either or both
Nice to have
• Clear, Bright lettering. Images of child or children enjoying reading
Should not have
• stereotypes

```html
<!DOCTYPE html>
<html lang="en">
<head>
<meta charset="utf-8">
<title>Pause Your Day And Browse – PYDB</title>
<link rel="stylesheet" href="https://fonts.googleapis.com/css2?family=Archivo+Black&family=Arimo:wght@700&display=swap">
<style>
  :root {
    --paper: #ffffff;
    --board: #2f2f2f;
    --board-light: #3d3d3d;
    --board-dark: #222222;
    --teal: #93d3cb;
    --white: #ffffff;
    --ink: #2a2a2a;
    --band: #1c1c1c;
  }
  html, body {
    margin: 0;
    padding: 0;
    width: 1200px;
    height: 776px;
    overflow: hidden;
    background: var(--paper);
  }
  .poster {
    position: relative;
    width: 1200px;
    height: 776px;
    background: var(--paper);
  }
  .board {
    position: absolute;
    left: 34px;
    top: 30px;
    width: 1132px;
    height: 714px;
    background:
      radial-gradient(ellipse at 60% 40%, var(--board-light) 0%, var(--board) 55%, var(--board-dark) 100%);
    overflow: hidden;
  }
  .acronym {
    position: absolute;
    left: 88px;
    top: 84px;
    width: 760px;
    height: 280px;
  }
  .acronym text {
    font-family: "Archivo Black", "Arial Black", sans-serif;
    font-size: 340px;
  }
  .title {
    position: absolute;
    left: 74px;
    top: 436px;
    margin: 0;
    font-family: "Arimo", Arial, sans-serif;
    font-weight: 700;
    font-size: 60px;
    line-height: 1.08;
    color: var(--teal);
    letter-spacing: 0.5px;
  }
  .date {
    position: absolute;
    left: 74px;
    top: 606px;
    margin: 0;
    font-family: "Arimo", Arial, sans-serif;
    font-weight: 700;
    font-size: 27px;
    color: var(--white);
  }
  .shadow-band {
    position: absolute;
    left: 692px;
    top: 540px;
    width: 440px;
    height: 130px;
    background: linear-gradient(90deg, rgba(28,28,28,0) 0%, var(--band) 18%, var(--band) 100%);
    clip-path: polygon(6% 0, 100% 0, 100% 100%, 6% 100%, 0 50%);
    opacity: 0.85;
  }
  .guild-mark {
    position: absolute;
    left: 982px;
    top: 42px;
    width: 114px;
    height: 114px;
    background: var(--white);
    display: flex;
    align-items: center;
    justify-content: center;
    text-align: center;
    box-sizing: border-box;
    padding: 8px;
    font-family: "Arimo", Arial, sans-serif;
    font-weight: 700;
    font-size: 14px;
    line-height: 1.2;
    color: var(--ink);
  }
  .union-mark {
    position: absolute;
    left: 962px;
    top: 586px;
    display: flex;
    align-items: center;
    gap: 12px;
    font-family: "Arimo", Arial, sans-serif;
    font-weight: 700;
    font-size: 27px;
    color: var(--white);
  }
  .union-mark .dot {
    width: 56px;
    height: 56px;
    border-radius: 50%;
    background: var(--white);
  }
</style>
</head>
<body>
  <main class="poster">
    <section class="board">
      <svg class="acronym" viewBox="0 0 760 280" role="img" aria-label="PYDB lettering filled with a photo of two children reading a book together">
        <defs>
          <linearGradient id="photo-tones" x1="0" y1="0" x2="1" y2="1">
            <stop offset="0" stop-color="#e9dccb"/>
            <stop offset="0.35" stop-color="#c9a98c"/>
            <stop offset="0.6" stop-color="#7fb9c9"/>
            <stop offset="1" stop-color="#3f6fa3"/>
          </linearGradient>
        </defs>
        <text x="8" y="262" textLength="744" lengthAdjust="spacingAndGlyphs"
              fill="url(#photo-tones)" stroke="#ffffff" stroke-width="3">PYDB</text>
      </svg>

      <div class="guild-mark">Coastline Shelfkeepers Guild</div>

      <h1 class="title">PAUSE YOUR DAY<br>AND BROWSE</h1>
      <p class="date">Monday, October 23, 2017</p>

      <div class="shadow-band"></div>
      <div class="union-mark"><span class="dot"></span><span class="union-name">KWNU</span></div>
    </section>
  </main>
</body>
</html>
```